依頼詳細
クリニックのHPです。
https://kitase-naika.jp
チラシはA4サイズです。
自分のイメージとして、こんなチラシが好き、こんなのは嫌という例を添付しますので参考にしてください。
添付した資料は全部使う必要はありません(特に、外観、内観予想図)。
ソノワで印刷しますので、ソノワが対応しているデータ形式でお願いします(ソノワにデータ作成テンプレートがあります)。
https://sonowa.com/guide/how-to-make-data/pamphlet/
クリニックがまだできていないので、外観予想図、内観予想図を添付します。
クリニック用のリーフレットデザインも別コンペで募集しています。
記載項目
開催日 2020年5月10日土曜日、場所、地図、アクセス
サイズ
A4
ページ数
片面
希望イメージ
シンプル 複雑
単色 カラフル
暗い 明るい
日常 高級
遊び心 厳粛
未来的 伝統的
女性的 男性的
希望する色
黄・オレンジ系、緑系、水色系
■ 選んだ理由

全体にバランスが良く、第一印象が良かったです。

■ 提案者全員のお礼・コメント

多くの皆様に応募していただき、ありがとうございます
良いデザイン案が多く、選ぶのに苦慮しました。今後も、仕事を依頼することがあると思いますが、よろしくお願いします。

```html
<!DOCTYPE html>
<html lang="ja">
<head>
<meta charset="utf-8">
<title>北瀬みずき内科 内覧会のご案内</title>
<link rel="stylesheet" href="https://fonts.googleapis.com/css2?family=Noto+Sans+JP:wght@400;500;700;900&display=swap">
<style>
:root{
  --navy:#1e3a8c;
  --blue:#2f6fc1;
  --sky:#d5ebf8;
  --peach:#fce6d6;
  --red:#e2352c;
  --ink:#333;
  --paper:#fff;
  --grey:#c9ccd1;
}
*{margin:0;padding:0;box-sizing:border-box}
html,body{width:857px;height:1200px;overflow:hidden;background:var(--paper)}
body{font-family:"Noto Sans JP",sans-serif;color:var(--ink);position:relative}
.flyer{position:relative;width:857px;height:1200px}

.header{position:absolute;left:30px;top:18px;display:flex;align-items:center;gap:22px}
.header__mark{width:60px;height:60px;border-radius:50%;background:var(--blue)}
.header__name{font-size:50px;font-weight:900;color:var(--navy);letter-spacing:2px;line-height:1}
.header__roman{font-size:15px;color:var(--navy);letter-spacing:1px;margin-top:6px;text-align:center}
.header__dept{font-size:22px;font-weight:700;color:var(--navy);margin-top:6px;text-align:center;letter-spacing:1px}

.intro{position:absolute;left:30px;top:138px;width:797px;height:182px;background:var(--peach);padding:10px 26px 8px;font-size:13.5px;line-height:1.6}
.intro__lead{text-align:center;font-weight:500;margin-bottom:2px}
.intro__em{color:var(--red);font-weight:700;font-size:15px}
.intro__sign{text-align:right;font-size:12px;margin-top:2px;padding-right:30px}

.profile{position:absolute;left:30px;top:330px;width:797px;height:118px}
.career{position:absolute;left:0;top:0;width:460px;font-size:11.5px;line-height:1.7}
.career__title,.society__title{font-weight:700;font-size:12px}
.career dl{display:grid;grid-template-columns:68px 1fr}
.society{position:absolute;left:470px;top:0;width:190px;font-size:10.5px;line-height:1.7}
.portrait{position:absolute;right:0;top:0;width:120px;height:116px;background:linear-gradient(#e8ecef,#b9c2c9)}

.event{position:absolute;left:0;top:458px;width:857px;height:118px;background:var(--sky)}
.event__title{position:absolute;left:44px;top:8px;font-size:40px;font-weight:900;color:var(--navy);letter-spacing:4px;line-height:1.2}
.event__date{position:absolute;left:44px;top:58px;font-size:42px;font-weight:700;color:var(--navy);letter-spacing:14px;line-height:1.2}

.access{position:absolute;left:30px;top:592px;width:797px;height:200px}
.map{position:absolute;left:0;top:0;width:470px;height:200px;background:linear-gradient(135deg,#eef2ee,#dde6dd)}
.info{position:absolute;left:500px;top:4px;font-size:12.5px;line-height:1.6}
.info__label{font-weight:700;color:var(--navy);font-size:13.5px}
.info p{margin-bottom:6px}

.building{position:absolute;left:30px;top:810px;width:270px;height:380px;background:linear-gradient(#cfe4f3,#9aa5ae)}

.hours{position:absolute;left:330px;top:835px;width:497px;font-size:13px}
.hours table{width:100%;border-collapse:collapse;text-align:center}
.hours th,.hours td{padding:5px 0;border-bottom:1px solid var(--grey)}
.hours th{font-weight:700;color:var(--navy)}
.hours td:first-child,.hours th:first-child{text-align:left;width:140px}
.hours__note{margin-top:8px;font-size:12.5px}
.hours__note b{color:var(--red)}

.search{position:absolute;left:330px;top:1100px;width:470px;height:66px;border:3px solid var(--navy);display:flex;align-items:center;justify-content:space-between;padding:0 18px}
.search__name{font-size:30px;font-weight:900;color:var(--navy)}
.search__url{position:absolute;left:0;right:0;bottom:-24px;text-align:center;font-size:15px;font-weight:700;color:var(--navy)}
</style>
</head>
<body>
<main class="flyer">

  <header class="header">
    <div class="header__mark"></div>
    <div>
      <div class="header__name">北瀬みずき内科</div>
      <div class="header__roman">Kitase Mizuki Clinic</div>
      <div class="header__dept">内科 / 脳神経内科 / 糖尿病</div>
    </div>
  </header>

  <section class="intro">
    <p class="intro__lead">地域の皆さまによりそう総合内科の「かかりつけ医」をめざして</p>
    <p><span class="intro__em">プライマリ・ケア（Primary care）とは、患者さんが抱える心身の問題を幅広く診療するトレーニングを受けた医師がおこなう医療です。</span>高血圧や糖尿病などの生活習慣病の治療が必要な方、頭痛やめまいで困っている方、物忘れや認知症が心配な方、原因がわからない体調不良がある方など、予防接種を受けたい方、治療が必要かどうか迷っている方など、さまざまな患者さんのご相談をしっかりと受けとめ、患者さん一人ひとりに寄りそう医療を提供し、気軽に相談していただけるクリニックづくりをめざしています。何卒よろしくお願い申し上げます。</p>
    <p class="intro__sign">院長　瑞木 康介</p>
  </section>

  <section class="profile">
    <div class="career">
      <p class="career__title">略歴</p>
      <dl>
        <dt>1994年</dt><dd>港南医科大学医学部卒業し、同大学附属病院にて研修</dd>
        <dt>2003年</dt><dd>博士号取得</dd>
        <dt>2006年より</dt><dd>地域中核病院総合内科に勤務し現在は総括診療部長</dd>
      </dl>
    </div>
    <div class="society">
      <p class="society__title">所属学会・資格</p>
      <p>日本内科学会 総合内科専門医</p>
      <p>日本神経学会 神経内科専門医</p>
      <p>日本糖尿病学会 専門医</p>
      <p>日本プライマリ・ケア学会認定医</p>
    </div>
    <div class="portrait" role="img" aria-label="院長のポートレート写真"></div>
  </section>

  <section class="event">
    <h1 class="event__title">内覧会開催</h1>
    <p class="event__date">2020年5月10日土曜日</p>
  </section>

  <section class="access">
    <div class="map" role="img" aria-label="北瀬駅からクリニックまでの周辺地図"></div>
    <div class="info">
      <p><span class="info__label">所在地</span><br>〒160-0000<br>東京都中央区北瀬2-14-8　北瀬ビル1階</p>
      <p><span class="info__label">アクセス</span><br>北瀬駅から徒歩10分<br>北瀬駅前バス停から徒歩2分</p>
    </div>
  </section>

  <div class="building" role="img" aria-label="クリニックの外観写真"></div>

  <section class="hours">
    <table>
      <tr><th>診療時間</th><th>月</th><th>火</th><th>水</th><th>木</th><th>金</th><th>土</th><th>日</th></tr>
      <tr><td>9:00 – 12:00</td><td>●</td><td>●</td><td>●</td><td>ー</td><td>●</td><td>●</td><td>ー</td></tr>
      <tr><td>14:30 – 18:00</td><td>●</td><td>●</td><td>●</td><td>ー</td><td>●</td><td>ー</td><td>ー</td></tr>
    </table>
    <p class="hours__note"><b>休診日</b>　木曜日・日曜・祝日</p>
  </section>

  <div class="search">
    <span class="search__name">北瀬みずき内科</span>
    <svg width="34" height="34" viewBox="0 0 34 34" aria-hidden="true"><circle cx="14" cy="14" r="10" fill="none" stroke="#1e3a8c" stroke-width="4"/><line x1="21" y1="21" x2="31" y2="31" stroke="#1e3a8c" stroke-width="5" stroke-linecap="round"/></svg>
    <span class="search__url">kitase-naika.jp</span>
  </div>

</main>
</body>
</html>
```